Veltrona Services

Double sided business cards with color on front and black and white on back. I have basic ideas and graphics, but am looking for someone to take them to the next level

```html
<!DOCTYPE html>
<html lang="en">
<head>
<meta charset="utf-8">
<title>Veltrona Services — Business Card</title>
<link rel="stylesheet" href="https://fonts.googleapis.com/css2?family=Cinzel:wght@500;600;700&display=swap">
<style>
  :root {
    --backdrop: #2c3032;
    --card: #ffffff;
    --ink: #111111;
    --gold-dark: #4f360a;
    --gold-mid: #9c7418;
    --gold-light: #d8b23a;
    --art-soft: #ece6f4;
    --art-mid: #d9d2ee;
  }
  * { margin: 0; padding: 0; box-sizing: border-box; }
  html, body {
    width: 1200px;
    height: 720px;
    overflow: hidden;
    background: var(--backdrop);
  }
  .canvas {
    position: relative;
    width: 1200px;
    height: 720px;
  }
  .card {
    position: absolute;
    background: var(--card);
    font-family: "Cinzel", Georgia, serif;
  }
  .card--front { left: 326px; top: 20px; width: 554px; height: 318px; }
  .card--back  { left: 327px; top: 389px; width: 551px; height: 313px; }

  .gold-text {
    background: linear-gradient(90deg, var(--gold-dark) 0%, var(--gold-mid) 30%, var(--gold-light) 55%, var(--gold-mid) 75%, var(--gold-light) 100%);
    -webkit-background-clip: text;
    background-clip: text;
    color: transparent;
  }

  .tagline {
    position: absolute;
    left: 0;
    right: 0;
    top: 40px;
    text-align: center;
    font-size: 30px;
    font-weight: 700;
    line-height: 33px;
    letter-spacing: 0.3px;
    text-transform: uppercase;
    white-space: nowrap;
  }

  .brand-mark {
    position: absolute;
    left: 0;
    right: 0;
    top: 132px;
    display: flex;
    flex-direction: column;
    align-items: center;
    gap: 12px;
  }
  .brand-mark__circle {
    width: 112px;
    height: 112px;
    border-radius: 50%;
    border: 18px solid var(--ink);
  }
  .brand-mark__name {
    font-size: 18px;
    font-weight: 700;
    color: var(--ink);
    text-transform: uppercase;
    letter-spacing: 0.5px;
  }

  .company-name {
    position: absolute;
    left: 0;
    right: 0;
    top: 20px;
    text-align: center;
    font-size: 33px;
    font-weight: 700;
    line-height: 40px;
    text-transform: uppercase;
    white-space: nowrap;
  }
  .contact-phone {
    position: absolute;
    left: 0;
    right: 0;
    top: 66px;
    text-align: center;
    font-size: 26px;
    font-weight: 600;
    line-height: 32px;
    color: var(--ink);
  }
  .network-art {
    position: absolute;
    left: 181px;
    top: 111px;
    width: 180px;
    height: 182px;
    background: linear-gradient(160deg, var(--art-soft) 0%, var(--art-mid) 100%);
  }
</style>
</head>
<body>
  <main class="canvas">
    <section class="card card--front">
      <h2 class="tagline gold-text">A Curated Experience All<br>That Is Promised Clarity</h2>
      <div class="brand-mark">
        <span class="brand-mark__circle" aria-hidden="true"></span>
        <span class="brand-mark__name">Veltrona Services</span>
      </div>
    </section>

    <section class="card card--back">
      <h1 class="company-name gold-text">Veltrona Services</h1>
      <p class="contact-phone">C : 555-014-2287</p>
      <div class="network-art" role="img" aria-label="Circular network illustration of coloured dots joined by fine lines"></div>
    </section>
  </main>
</body>
</html>
```